Medical Marihuana Ziplock Bag Mockup Design

We seek skilled and professional designer for medical marihuana ziplock bag packaging design. We need a modern, minimal, clean Design with the name productname: Plumo - Endproduct will be a ziplock bag (see attachment) samples.
Product may but must not contain a cannabis leaf in Design7Logo

Target Market(s)

young audience

Industry/Entity Type

Medical

Logo Text

P L U M O

Font styles to use
Serif
Sans Serif

Colors
9bcb3c
abd037
cadf82
ffc214
fece3e
fee18a
6b449b
886aae
b8a6cd

Requirements
Nice to have
• Can but must not contain a minimal cannabis leaf as abstract sign

```html
<!DOCTYPE html>
<html lang="de">
<head>
<meta charset="utf-8">
<title>Plumo – Medical Marijuana Pouch</title>
<link rel="stylesheet" href="https://fonts.googleapis.com/css2?family=Cormorant+Garamond:wght@500&family=Roboto+Slab:wght@500&family=Open+Sans:wght@400;600;700&display=swap">
<style>
  :root {
    --canvas-bg: #ecebe8;
    --pouch-white: #f4f5f4;
    --pouch-silver: #dfe2e0;
    --green-brand: #4f9d33;
    --green-deep: #23692a;
    --green-mid: #3b8a34;
    --green-bright: #7fbf3f;
    --green-soft: #8fcb5a;
    --green-pale: #b9dc8c;
    --text-light: #eef5ea;
    --text-muted: #d8e8d0;
  }
  * { margin: 0; padding: 0; box-sizing: border-box; }
  html, body { width: 1200px; height: 1200px; overflow: hidden; }
  body {
    background: var(--canvas-bg);
    position: relative;
    font-family: "Open Sans", Arial, sans-serif;
  }
  .pouch {
    position: absolute;
    left: 272px; top: 70px;
    width: 656px; height: 1060px;
    overflow: hidden;
    background: linear-gradient(180deg, var(--pouch-white) 0%, var(--pouch-silver) 40%, var(--pouch-white) 46%);
  }
  .zip-line {
    position: absolute; left: 0; right: 0; top: 167px; height: 5px;
    background: var(--green-bright);
  }
  .zip-band {
    position: absolute; left: 0; right: 0; top: 186px; height: 22px;
    background: linear-gradient(180deg, var(--green-mid), var(--green-brand));
  }
  .age-mark {
    position: absolute; right: 28px; top: 226px;
    font-size: 26px; color: var(--green-brand); font-weight: 400;
  }
  .brand-name {
    position: absolute; left: 0; right: 0; top: 288px;
    text-align: center;
    font-family: "Cormorant Garamond", Georgia, serif;
    font-weight: 500;
    font-size: 124px; line-height: 1;
    letter-spacing: 4px;
    color: var(--green-brand);
  }
  .front-panel {
    position: absolute; left: 0; right: 0; top: 488px; bottom: 0;
    background: linear-gradient(180deg, var(--green-deep) 0%, var(--green-mid) 30%, var(--green-soft) 48%, var(--green-mid) 70%, var(--green-deep) 100%);
  }
  .product-pill {
    position: absolute; left: 50%; top: 491px; transform: translateX(-50%);
    width: 330px; height: 50px; border-radius: 12px;
    background: linear-gradient(180deg, var(--green-bright), var(--green-brand));
    border: 2px solid var(--green-pale);
    color: #fff;
    font-family: "Roboto Slab", Georgia, serif; font-weight: 500;
    font-size: 26px; line-height: 46px; text-align: center;
  }
  .origin-line {
    position: absolute; left: 0; right: 0; top: 555px;
    text-align: center; color: var(--text-light);
    font-size: 18px; letter-spacing: 0.5px;
  }
  .tagline {
    position: absolute; left: 0; right: 0; top: 604px;
    text-align: center; color: var(--green-bright);
    font-size: 19px;
  }
  .divider {
    position: absolute; left: 0; right: 0; top: 646px; height: 2px;
    background: rgba(255,255,255,0.7);
  }
  .leaf-art {
    position: absolute; left: 13px; top: 672px; width: 270px; height: 340px;
    background: radial-gradient(ellipse at 50% 45%, rgba(120,190,90,0.55), rgba(60,140,60,0.25) 60%, rgba(0,0,0,0) 80%);
  }
  .warning-rule {
    position: absolute; left: 290px; top: 668px; width: 2px; height: 302px;
    background: rgba(255,255,255,0.55);
  }
  .health-warning {
    position: absolute; left: 303px; top: 676px; width: 345px;
    color: var(--text-muted); font-size: 19.5px; line-height: 27px;
  }
  .net-weight {
    position: absolute; left: 26px; top: 985px;
    color: #fff; font-weight: 700; font-size: 36px;
  }
  .medical-cross { position: absolute; left: 470px; top: 985px; width: 64px; height: 64px; }
  .strain-list {
    position: absolute; left: 578px; top: 962px; list-style: none;
    color: var(--text-light); font-size: 11px; letter-spacing: 0.5px;
  }
  .strain-list li { display: flex; align-items: center; gap: 6px; height: 23px; }
  .strain-list .box { width: 13px; height: 13px; border: 1.5px solid #fff; background: rgba(255,255,255,0.3); }
</style>
</head>
<body>
  <section class="pouch">
    <div class="zip-line"></div>
    <div class="zip-band"></div>
    <div class="age-mark">18+</div>
    <div class="brand-name">PLUMO</div>

    <div class="front-panel"></div>
    <div class="product-pill">Medical Marijuana</div>
    <div class="origin-line">100% SCHWEIZER HANF</div>
    <div class="tagline">Product auf pflanzlicher Basis ohne Tabak</div>
    <div class="divider"></div>

    <div class="leaf-art" role="img" aria-label="Faint green cannabis leaf illustration"></div>
    <div class="warning-rule"></div>
    <p class="health-warning">
      Rauchen fügt ihnen und den Menschen in ihrer Umgebung erheblichen Schaden zu.<br>
      Fumer nuit Gravement à votre santé et à celle de votre entourage.<br>
      Il fumo daneggia gravemente te e chi ti sta intorno.
    </p>

    <div class="net-weight">10g</div>
    <svg class="medical-cross" viewBox="0 0 64 64" aria-hidden="true">
      <path d="M22 0h20v22h22v20H42v22H22V42H0V22h22z" fill="#6fbf3c"/>
    </svg>
    <ul class="strain-list">
      <li><span class="box"></span>INDICA</li>
      <li><span class="box"></span>SATIVA</li>
      <li><span class="box"></span>HYBRID</li>
    </ul>
  </section>
</body>
</html>
```